Local Motorsports Photography Business Card Design

Looking for a Logo and Business Card design for my father who is a local photographer based in Perth operating under the business name "KLR Photography". Specializing in Motorsports (Torque Racers/Hyperwheels/Corvan Trial) and events photography.
Would like it to look professional, while still maintaining a local/personal feel. Color\Design of the Logo and Card are open to your own interpretation, but should limit the color scheme to around 2-3 colors.
Design should be a logo one side and contact details on the rear. The website currently is very simple and a generic template and should not be used as a basis for design.
Industry/Entity Type
Business
Contact Information for Business Card
Name: Malcolm Purdie
Website: www.klrphotography-example.com.au
Email: malcolm@klrphotography-example.com.au
Phone: 0471 629 385
Look and feel
Each slider illustrates characteristics of the customer's brand and the style your logo design should communicate.

```html
<!DOCTYPE html>
<html lang="en">
<head>
<meta charset="utf-8">
<title>KLR Photography – Business Card</title>
<link rel="stylesheet" href="https://fonts.googleapis.com/css2?family=Open+Sans:wght@400;700&display=swap">
<style>
  :root {
    --backdrop: #e7e3dd;
    --asphalt-dark: #1f1f1f;
    --asphalt-mid: #3c3c3c;
    --asphalt-light: #6a6a6a;
    --paper-light: #efefef;
    --paper-mid: #d4d4d4;
    --ink: #3a3a3a;
    --logo-white: #ffffff;
    --flag-dark: #1a1a1a;
    --flag-light: #e9e9e9;
  }
  * { box-sizing: border-box; margin: 0; padding: 0; }
  html, body {
    width: 1200px; height: 900px; overflow: hidden;
    background: var(--backdrop);
    font-family: "Open Sans", Arial, sans-serif;
  }
  .canvas { position: relative; width: 1200px; height: 900px; }

  .card {
    position: absolute;
    width: 560px; height: 320px;
    overflow: hidden;
    box-shadow: 0 6px 18px rgba(0,0,0,0.22);
  }

  /* Rear: contact details */
  .card--rear { left: 70px; top: 110px; background: var(--asphalt-dark); }
  .card--rear .track-band {
    position: absolute; left: 0; right: 0; height: 70px;
    background: linear-gradient(180deg, var(--asphalt-dark), var(--asphalt-mid) 50%, var(--asphalt-dark));
  }
  .card--rear .track-band--top { top: 0; }
  .card--rear .track-band--bottom { bottom: 0; }
  .card--rear .details-panel {
    position: absolute; left: 0; right: 0; top: 70px; bottom: 70px;
    background: radial-gradient(ellipse at 50% 50%, var(--paper-light) 40%, var(--paper-mid) 100%);
    padding: 26px 28px 0;
  }
  .contact-list { list-style: none; }
  .contact-list li {
    font-size: 17px; line-height: 1.9; color: var(--ink);
    text-transform: uppercase; letter-spacing: 0.3px; white-space: nowrap;
  }

  /* Front: logo */
  .card--front {
    left: 570px; top: 470px;
    background: linear-gradient(160deg, var(--asphalt-mid) 0%, var(--asphalt-light) 45%, var(--asphalt-dark) 100%);
  }
  .card--front .track-strip {
    position: absolute; left: 230px; top: 90px; width: 320px; height: 70px;
    background: linear-gradient(180deg, transparent, rgba(0,0,0,0.35) 30%, rgba(0,0,0,0.35) 70%, transparent);
  }
  .card--front .flag-wave { position: absolute; left: 0; top: 0; width: 560px; height: 320px; }
  .logo {
    position: absolute; left: 260px; top: 78px; width: 270px;
    text-align: center; color: var(--logo-white); font-weight: 700;
    text-transform: uppercase; line-height: 1.05;
  }
  .logo__mark { display: block; font-size: 52px; letter-spacing: 4px; }
  .logo__word { display: block; font-size: 30px; letter-spacing: 3px; }
</style>
</head>
<body>
<main class="canvas">

  <section class="card card--rear" aria-label="Business card rear">
    <div class="track-band track-band--top" role="img" aria-label="Tyre track texture on asphalt"></div>
    <div class="details-panel">
      <ul class="contact-list">
        <li>Name: Malcolm Purdie</li>
        <li>Phone: 0471 629 385</li>
        <li>Website: www.klrphotography-example.com.au</li>
        <li>Email:malcolm@klrphotography-example.com.au</li>
      </ul>
    </div>
    <div class="track-band track-band--bottom" role="img" aria-label="Tyre track texture on asphalt"></div>
  </section>

  <section class="card card--front" aria-label="Business card front">
    <div class="track-strip" role="img" aria-label="Tyre track mark behind the logo"></div>
    <svg class="flag-wave" viewBox="0 0 560 320" role="img" aria-label="Waving black and white chequered flag">
      <defs>
        <linearGradient id="flagTone" x1="0" y1="0" x2="1" y2="1">
          <stop offset="0" stop-color="var(--flag-light)"/>
          <stop offset="0.5" stop-color="#8a8a8a"/>
          <stop offset="1" stop-color="var(--flag-dark)"/>
        </linearGradient>
      </defs>
      <path d="M0 160 C120 140 220 200 300 250 C360 290 420 300 470 320 L0 320 Z" fill="url(#flagTone)"/>
    </svg>
    <div class="logo">
      <span class="logo__mark">KLR</span>
      <span class="logo__word">Photography</span>
    </div>
  </section>

</main>
</body>
</html>
```